Breakthrough memory supplement needs an eye catching label design

Brightwater Goods, LLC needs an eye catching label design for Cerovant, an Superior Mind and Recall Blend

Completed label designs should be saved as .EPS files with all fonts outlined.
We can also accept Adobe Photoshop or .JPG files at 300dpi.
All files MUST include the .0625 bleed on all sides.

Target Market(s)

people 45 and older that are noticing there memory is not as good as it once was

Industry/Entity Type

Supplement

Colors

Designer to choose colors to be used in the design.

Requirements
Must have
• Cerovant
• Superior Mind and Recall Blend
Nice to have
• look sciencey/ medical
Should not have
• cutesy

```html
<!DOCTYPE html>
<html lang="en">
<head>
<meta charset="utf-8">
<title>Cerovant Label</title>
<link rel="stylesheet" href="https://fonts.googleapis.com/css2?family=Arimo:ital,wght@0,400;0,700;1,400&family=Archivo+Black&family=Montserrat:wght@500;800&family=Oswald:wght@500&family=Roboto+Condensed:wght@700&display=swap">
<style>
  :root {
    --teal: #1ea79b;
    --blue: #1e7cc0;
    --label-bg: #f0f1f2;
    --ink: #1b1b1b;
    --page: #ffffff;
  }
  * { box-sizing: border-box; margin: 0; padding: 0; }
  html, body { width: 1144px; height: 1200px; overflow: hidden; background: var(--page); }
  .label {
    position: absolute; left: 0; top: 395px; width: 1144px; height: 411px;
    background: var(--label-bg); overflow: hidden;
    font-family: "Arimo", Arial, sans-serif; color: var(--ink);
  }
  .bands { position: absolute; inset: 0; }
  .left-panel { position: absolute; left: 30px; top: 38px; width: 262px; font-size: 10px; line-height: 11.2px; letter-spacing: -0.15px; text-align: justify; }
  .left-panel p { margin-bottom: 10px; }
  .left-panel b { font-weight: 700; }
  .fda-box {
    position: absolute; left: 30px; top: 277px; width: 222px; border: 1.5px solid var(--ink);
    padding: 2px 4px; font-size: 7.8px; line-height: 9.4px; font-weight: 700;
  }
  .distributor { position: absolute; left: 33px; top: 333px; font-family: "Roboto Condensed", "Arial Narrow", sans-serif; font-weight: 700; font-size: 13px; line-height: 16.5px; letter-spacing: -0.2px; }
  .brand { position: absolute; left: 368px; top: 138px; width: 420px; height: 140px; }
  .brand-mark { position: absolute; left: 292px; top: 0; width: 96px; height: 96px; border-radius: 50%; background: var(--teal); opacity: 0.85; }
  .brand-name { position: absolute; left: 0; top: 46px; font-family: "Montserrat", sans-serif; font-weight: 800; font-size: 66px; line-height: 66px; color: var(--teal); letter-spacing: -1px; }
  .brand-tagline { position: absolute; left: 22px; top: 112px; font-family: "Montserrat", sans-serif; font-weight: 500; font-size: 16.5px; color: var(--blue); white-space: nowrap; }
  .front-footer { position: absolute; left: 355px; width: 411px; top: 359px; text-align: center; color: #fff; font-family: "Oswald", sans-serif; font-weight: 500; font-size: 14px; line-height: 17px; }
  .facts { position: absolute; left: 848px; top: 35px; width: 259px; border: 1.5px solid var(--ink); background: #fff; padding: 1px 5px 0; }
  .facts h2 { font-family: "Archivo Black", sans-serif; font-weight: 400; font-size: 24px; line-height: 27px; letter-spacing: -0.3px; white-space: nowrap; }
  .facts .serving { font-size: 10.8px; line-height: 11.5px; padding-left: 2px; }
  .facts .rule-thick { border-top: 5px solid var(--ink); margin: 2px 0 1px; }
  .facts .head { font-size: 8px; line-height: 11px; padding-left: 2px; border-bottom: 2px solid var(--ink); }
  .facts table { width: 100%; border-collapse: collapse; font-size: 10.6px; line-height: 12.2px; }
  .facts td { border-bottom: 1px solid var(--ink); padding: 1px 0 0; vertical-align: top; white-space: nowrap; }
  .facts tr.main td { border-bottom: none; }
  .facts td.amt { text-align: right; padding-right: 6px; }
  .facts td.dv { width: 8px; text-align: right; }
  .facts .indent { padding-left: 5px; }
  .facts tr:last-child td { border-bottom: 3px solid var(--ink); }
  .facts .foot { font-size: 10.6px; line-height: 13px; }
  .right-notes { position: absolute; left: 848px; top: 287px; width: 264px; font-size: 10px; line-height: 10.8px; text-align: justify; }
  .right-notes .strong { font-weight: 700; }
  .right-notes .warn { font-weight: 700; margin-top: 14px; }
</style>
</head>
<body>
  <section class="label">
    <svg class="bands" width="1144" height="411" viewBox="0 0 1144 411" aria-hidden="true">
      <path d="M0 0 H1144 V28 H790 V44 Q790 58 776 58 H369 Q355 58 355 44 V28 H0 Z" fill="var(--teal)"/>
      <path d="M0 385 H355 V370 Q355 353 372 353 H749 Q766 353 766 370 V385 H1144 V411 H0 Z" fill="var(--blue)"/>
    </svg>

    <div class="left-panel">
      <p><b>SUGGESTED USE:</b> 1 capsule taken 1 to 2 times daily preferably with meals or as directed by a healthcare professional.</p>
      <p><b>CAUTION:</b> Do not exceed recommended dose. St. John's Wort may contribute to photosensitivity resulting in skin irritation and redness in persons exposed to strong sunlight or tanning booths. Avoid use in patients at risk of bleeding, taking anticoagulants, or with clotting disorders, based on case reports of bleeding. Discontinue use 2-3 weeks prior to some surgical and dental procedures due to increased risk of bleeding. Avoid use in couples who are trying to conceive, based on theoretical reduction of fertility. Pregnant or nursing mothers, children under 18, individuals with history of seizure, taking MAO inhibiting drugs, or with a known medical condition should consult a physician before using this or any dietary supplement. This product is manufactured and packaged in a facility which may also process milk, soy, wheat, egg, peanuts, tree nuts, fish and crustacean shellfish.</p>
    </div>
    <div class="fda-box">†These statements have not been evaluated by the Food &amp; Drug Administration. This product is not intended to diagnose, treat, cure or prevent any disease.</div>
    <div class="distributor">Distributed by:<br>Company Name<br>Full Address and Phone</div>

    <div class="brand">
      <div class="brand-mark" role="img" aria-label="Brain illustration in teal line art"></div>
      <div class="brand-name">Cerovant</div>
      <div class="brand-tagline">Superior Mind and Recall Blend</div>
    </div>
    <div class="front-footer">DIETARY SUPPLEMENT<br>30 CAPSULES</div>

    <div class="facts">
      <h2>Supplement Facts</h2>
      <div class="serving">Serving Size 1 Capsule<br>Servings Per Container: 30</div>
      <div class="rule-thick"></div>
      <div class="head">Amt Per Serv. &nbsp;&nbsp;%DV/RDI</div>
      <table>
        <tr><td><i>Ginkgo biloba</i> Leaf (24% extract)</td><td class="amt">50mg</td><td class="dv">*</td></tr>
        <tr class="main"><td>Phosphatidylserine 4% Complex</td><td class="amt">125mg</td><td class="dv">*</td></tr>
        <tr><td colspan="3" class="indent">(consisting of Lecithin and Phosphatidylserine)</td></tr>
        <tr><td>N-Acetyl L-Carnitine HCl</td><td class="amt">50mg</td><td class="dv">*</td></tr>
        <tr class="main"><td>St. John's Wort (0.3% extract)</td><td class="amt">250mg</td><td class="dv">*</td></tr>
        <tr><td colspan="3" class="indent">(flower heads)</td></tr>
        <tr><td>L-Glutamine</td><td class="amt">150mg</td><td class="dv">*</td></tr>
        <tr class="main"><td><i>Bacopa monnieri</i> Leaf Extract</td><td class="amt">120mg</td><td class="dv">*</td></tr>
        <tr><td colspan="3" class="indent">(20% bacosides)</td></tr>
        <tr><td class="indent">inpocetine (seeds)</td><td class="amt">2mg</td><td class="dv">*</td></tr>
        <tr><td>Huperzine-A (aerial plant)</td><td class="amt">10mcg</td><td class="dv">*</td></tr>
      </table>
      <div class="foot">*Daily Value not established.</div>
    </div>
    <div class="right-notes">
      <p><span class="strong">Other ingredients:</span> Gelatin (bovine), microcrystalline cellulose, vegetable magnesium stearate, and silicon dioxide.</p>
      <p class="strong">ALLERGEN WARNING: CONTAINS SOY (LECITHIN).</p>
      <p class="warn">KEEP OUT OF THE REACH OF CHILDREN.<br>DO NOT USE IF SAFETY SEAL IS DAMAGED OR MISSING. STORE IN A COOL, DRY PLACE.</p>
    </div>
  </section>
</body>
</html>
```